Heath Weight Loss Retreat Website

The brief:
PineLoop is a provider of health & weight loss retreats and wish to redesign their main website. The website needs to provide detailed information about the company’s services whilst gathering the maximum number of leads possible. The website does not aim to get clients to ‘book now’ but to request further information, or ask a question generating a lead/opportunity for the business.

Primary objectives of website
• Gather leads for products (not necessarily to book at that point, but to ‘request more info’)
• Provide detailed information about the health and fitness programs on offer

Demographic Considerations
• Target age group: 30-50
• Predominant client base are female but website should be gender neutral due to some men attending

Design considerations
• Essentially selling ‘travel experiences’ and ‘life transformations’ so needs to be lots of images to display (similar to a hotel website for example)
• Images need to display real people – i.e. larger people, rather than super thin
• Not too much use of flash
• SEO friendly (we have good rankings at present)
• Will be implemented into Joomla, so please consider this on the design
• Colours should be ‘warm’ and ‘friendly’ and gender neutral

Project Requirements & Expectations
Please supply your design ideas with:
• At least 1 (preferably more) homepage examples
• At least 1 (preferably more) internal page examples
Once a preferred design has been selected the following will be produced, tweaked and approved:
• Homepage + 1 internal landing page + 1 internal main page + 1 contact page + 1 info request page

Attachments
We have attached both a homepage and internal page example which demonstates the type of content needed and the calls to action. This is for demonstration purposes only so please ignore colours, fonts, etc and provide your best designs based on a general layout as per attached.

Images:
A selection of example images has been attached. For the homepage images of the retreats themselves should be used alongside images of ‘larger people’.

Further information:
Please contact Simon Thackery at simon.thackery@coralbeaconfiles.com.au

Target Market(s)

Overweight females aged 30-50 are the main target market. However must be gender neutral due to some men using product.

Industry/Entity Type

Weight

Requirements
Should not have
• Not too much flash

```html
<!DOCTYPE html>
<html lang="en">
<head>
<meta charset="utf-8">
<title>PineLoop Weight Loss Retreat</title>
<link href="https://fonts.googleapis.com/css2?family=Arimo:wght@400;700&family=Tinos:ital@1&display=swap" rel="stylesheet">
<style>
:root{
  --green:#8cc21a;
  --green-pale:#eef7c8;
  --green-panel:#e2f3a0;
  --green-column:#d6eb8e;
  --orange:#f0920f;
  --orange-deep:#e2730a;
  --orange-light:#f6b24a;
  --sea:#4d93c4;
  --sand:#d9cdb0;
  --ink:#222;
  --brand-ink:#3a3a3a;
  --gold:#e6b23a;
}
*{box-sizing:border-box;margin:0;padding:0}
html,body{width:1035px;height:1200px;overflow:hidden}
body{font-family:"Arimo",Arial,sans-serif;color:var(--ink);background:var(--green-pale);position:relative}
.abs{position:absolute}

/* Header */
.site-header{position:absolute;left:0;top:0;width:1035px;height:423px;background:linear-gradient(100deg,#fff 0%,#fff 38%,#cfe58a 62%,var(--green) 80%)}
.brand{left:52px;top:14px}
.brand-name{font-weight:700;font-size:32px;color:var(--brand-ink);letter-spacing:.5px}
.hero{left:0;top:62px;width:1035px;height:332px;border-top-left-radius:80px;overflow:hidden;
  background:linear-gradient(180deg,#cfe3f1 0%,#9ec6e0 30%,var(--sea) 55%,#7aa9c2 70%,var(--sand) 100%)}
.hero-people{left:0;top:62px;width:428px;height:332px;border-top-left-radius:80px;background:linear-gradient(160deg,#8a7a6c,#a0483c 70%,#8c2b2b)}
.hero-runner{left:800px;top:120px;width:100px;height:274px;border-radius:40px 40px 0 0;background:linear-gradient(180deg,#c49a7a,#3fb0d8 45%,#222 90%)}
.nav-group{top:26px;width:140px}
.nav-tab{height:32px;background:linear-gradient(180deg,var(--orange-light),var(--orange));border-radius:6px 6px 0 0;color:#fff;font-size:11.5px;padding:10px 0 0 11px}
.nav-list{height:152px;background:rgba(255,255,255,.72);list-style:none;padding:10px 0 0 11px}
.nav-list li{font-size:10px;color:#7fae1e;line-height:16px}
.nav-list li::before{content:"• "}
.promo{left:918px;top:22px;width:76px;height:76px;background:var(--orange);transform:rotate(-12deg);color:#fff;text-align:center;padding-top:12px;box-shadow:2px 3px 4px rgba(0,0,0,.25)}
.promo b{display:block;font-weight:400;font-size:19px}
.promo span{font-size:10px;line-height:11px;display:block}
.promo-cta{left:916px;top:122px;width:119px;height:20px;border:1px solid #fff;border-right:none;color:#fff;font-size:11.5px;padding:3px 0 0 18px}
.hero-card{left:456px;top:240px;width:410px;height:154px;background:rgba(255,255,255,.78);border:1px solid #eee;text-align:center;padding-top:38px}
.hero-title{font-family:"Tinos",serif;font-style:italic;font-weight:400;font-size:30px;color:#111}
.hero-text{font-size:16px;line-height:20px;margin-top:8px;color:#222}
.quote-bar{left:0;top:394px;width:1035px;height:29px;background:#fff}
.quote{left:38px;top:398px;font-size:13px}
.lead-cta{left:656px;top:388px;width:379px;height:28px;background:linear-gradient(90deg,#fff 0%,var(--orange-light) 12%,var(--orange) 40%);color:#fff;font-size:13.5px;padding:5px 0 0 28px}

/* Content panel */
.panel{left:57px;top:446px;width:917px;height:581px;background:var(--green-panel)}
.panel-head{left:57px;top:446px;width:917px;height:26px;background:linear-gradient(90deg,#d1ea7e,#c4e46a);font-size:14px;font-weight:400;padding:10px 0 0 12px;height:30px}
.side-menu{left:66px;top:492px;list-style:none}
.side-menu li{font-size:11px;line-height:20px}
.side-menu li::before{content:"•";margin-right:6px}
.side-rule{left:122px;top:510px;width:226px;border-top:1px dashed #555}
.cta-btn{left:57px;width:272px;height:31px;background:linear-gradient(180deg,var(--orange-light),var(--orange));color:#fff;font-size:12.5px;padding:9px 0 0 40px;clip-path:polygon(0 0,100% 0,90% 100%,0 100%)}
.side-photo{left:67px;top:840px;width:276px;height:187px;background:linear-gradient(150deg,#6b5a52,#b04135 60%,#8e2424)}
.itinerary{left:344px;top:484px;width:351px;height:527px;background:linear-gradient(90deg,#c5df78,var(--green-column) 25%,#e3f4a4)}
.day{position:absolute;left:371px;font-size:10.5px}
.day-text{position:absolute;left:437px;width:238px;font-size:10px;line-height:18px;color:#333}
.place{font-size:11px;color:#333}
.photo{background:#fff;padding:8px;box-shadow:3px 4px 7px rgba(0,0,0,.35)}
.photo div{width:100%;height:100%}
.ph-mountain{left:738px;top:546px;width:250px;height:180px;transform:rotate(-5deg)}
.ph-mountain div{background:linear-gradient(180deg,#a6c6e2 0%,#c9a078 45%,#5e7a4e 75%,#3b5238)}
.ph-coast{left:700px;top:756px;width:262px;height:186px;transform:rotate(4deg)}
.ph-coast div{background:linear-gradient(200deg,#7cc0e6 0%,#2d9bb8 35%,#2c7a5a 60%,#356b37)}

/* Footer */
.site-footer{left:0;top:1055px;width:1035px;height:145px;background:var(--orange)}
.footer-inner{left:12px;top:1070px;width:996px;height:100px;background:linear-gradient(90deg,var(--orange-light),#fde9cc 40%,#fff 70%)}
.social{top:1084px;width:17px;height:17px;border-radius:3px}
.footer-links{left:50px;top:1110px;width:436px;height:54px;background:var(--orange);padding:3px 6px;display:grid;grid-template-columns:repeat(3,1fr);gap:3px}
.footer-links a{background:var(--orange-deep);color:#fff;font-size:12px;text-decoration:none;padding:3px 0 0 7px}
.footer-brand{left:820px;top:1094px}
.footer-brand .brand-name{font-size:27px}
.copyright{left:737px;top:1136px;font-size:12px}
</style>
</head>
<body>

<header class="site-header">
  <div class="abs hero" role="img" aria-label="Beach and sea under a clear sky"></div>
  <div class="abs hero-people" role="img" aria-label="Smiling couple embracing on the beach"></div>
  <div class="abs hero-runner" role="img" aria-label="Woman jogging along the shore"></div>

  <div class="abs brand"><span class="brand-name">PineLoop</span></div>

  <nav>
    <div class="abs nav-group" style="left:427px">
      <div class="nav-tab">The Best Programs</div>
      <ul class="nav-list"><li>Weight Loss Retreat</li><li>Residential Boot Camp</li><li>Fitness Days</li><li>At home program</li><li>Local group exercise</li></ul>
    </div>
    <div class="abs nav-group" style="left:586px">
      <div class="nav-tab">The Best Locations</div>
      <ul class="nav-list"><li>Blue Mountains, NSW</li><li>Sunshine Coast, QLD</li><li>What clients say....</li><li>Local Programs</li></ul>
    </div>
    <div class="abs nav-group" style="left:745px">
      <div class="nav-tab">Act now and get results</div>
      <ul class="nav-list"><li>Why choose PineLoop</li><li>Expert Team</li><li>What clients say...</li><li>Contact us</li></ul>
    </div>
  </nav>

  <div class="abs promo"><b>FREE</b><span>PineLoop<br>Magazine</span></div>
  <div class="abs promo-cta">Request now</div>

  <div class="abs hero-card">
    <h1 class="hero-title">Weight Loss Retreat</h1>
    <p class="hero-text">Lasting weight loss and lifestyle change for people<br>of all ages, shapes, sizes and fitness level</p>
  </div>

  <div class="abs quote-bar"></div>
  <p class="abs quote">“The best weight loss of my life”&nbsp;&nbsp; by Marla Quinton</p>
  <div class="abs lead-cta">Request more informations...</div>
</header>

<main>
  <section class="abs panel"></section>
  <h2 class="abs panel-head">The Best Locations</h2>
  <svg class="abs" style="left:57px;top:468px" width="400" height="28" viewBox="0 0 400 28" aria-hidden="true">
    <path d="M0 20 Q170 4 340 12 Q200 10 0 26Z" fill="var(--orange)"/>
  </svg>

  <ul class="abs side-menu">
    <li>Overview</li><li>Program Details</li><li>Available locations</li><li>Is it suitable for you?</li><li>Typical Day</li><li>Great Food</li><li>Valuable education</li><li>Lasting results</li><li>Photo Gallery</li><li>Testimonials</li>
  </ul>
  <div class="abs side-rule"></div>

  <div class="abs cta-btn" style="top:699px">Dates and Rates</div>
  <div class="abs cta-btn" style="top:741px">Book Now</div>
  <div class="abs cta-btn" style="top:784px">Request a FREE Information pack...</div>

  <div class="abs side-photo" role="img" aria-label="Happy couple, the woman holding a red rose"></div>

  <section class="abs itinerary"></section>
  <span class="day" style="top:497px">Day 1</span>
  <p class="day-text" style="top:493px">Arriving at the retreat, settle into your room, meet the team and enjoy a relaxed welcome dinner with the group.</p>
  <p class="day-text" style="top:585px">Gentle morning walk along the trails, then a healthy breakfast together.</p>
  <p class="day-text" style="top:640px">Afternoon workshop on mindful eating and planning simple balanced meals.</p>
  <span class="day" style="top:699px">Day 2</span>
  <p class="day-text" style="top:695px">Sunrise stretch and light circuit training at your own pace today.</p>
  <p class="day-text" style="top:750px">Cooking class with our chef, learning fresh and easy family recipes.</p>
  <p class="day-text" style="top:805px">Free time to relax, swim or book a soothing massage session.</p>
  <p class="day-text" style="top:860px">Evening talk on sleep, stress and building habits that really last.</p>
  <span class="day" style="top:937px">Day 2</span>
  <p class="day-text" style="top:933px">Final group hike, progress check with your coach and a farewell lunch before heading home feeling refreshed.</p>

  <p class="abs place" style="left:705px;top:497px">BLUE MOUNTAIN</p>
  <svg class="abs" style="left:699px;top:511px" width="135" height="26" viewBox="0 0 135 26" aria-label="5 stars">
    <defs><polygon id="star" points="13,1 16.5,9 25,9.5 18.5,15 20.5,24 13,19 5.5,24 7.5,15 1,9.5 9.5,9" fill="var(--gold)" stroke="#b88a22" stroke-width="1"/></defs>
    <use href="#star"/><use href="#star" x="27"/><use href="#star" x="54"/><use href="#star" x="81"/><use href="#star" x="108"/>
  </svg>
  <div class="abs photo ph-mountain"><div role="img" aria-label="Blue Mountains sandstone cliffs above forested valley"></div></div>
  <div class="abs photo ph-coast"><div role="img" aria-label="Aerial view of Sunshine Coast beach and headland"></div></div>
  <p class="abs place" style="left:695px;top:950px">SUNSHINE COAST</p>
  <svg class="abs" style="left:696px;top:968px" width="135" height="26" viewBox="0 0 135 26" aria-label="5 stars">
    <use href="#star"/><use href="#star" x="27"/><use href="#star" x="54"/><use href="#star" x="81"/><use href="#star" x="108"/>
  </svg>
</main>

<footer>
  <div class="abs site-footer"></div>
  <div class="abs footer-inner"></div>
  <span class="abs social" style="left:58px;background:#3b5998"></span>
  <span class="abs social" style="left:87px;background:#4cb3e0"></span>
  <span class="abs social" style="left:116px;background:var(--orange-deep)"></span>
  <nav class="abs footer-links">
    <a href="#">About Us</a><a href="#">The Best Programs</a><a href="#">Book Now</a>
    <a href="#">Resuts for...</a><a href="#">Privacy</a><a href="#">Contact Us</a>
  </nav>
  <div class="abs footer-brand"><span class="brand-name">PineLoop</span></div>
  <p class="abs copyright">Copyright © 2011 PineLoop. All rights reserved.</p>
</footer>

</body>
</html>
```